Business Card Design Project

I want my business cards to stand and feel timeless! I also want people to get their hands on them and freak out over how cool these are, I already have a logo i just want a very cool card design! this is for a makeup artist and maybe one day a line of cosmetics.

Target Market(s)

I want this to target women from 18 to 45

Industry/Entity Type

Business

Font styles to use
Decorative
Script

Colors

Designer to choose colors to be used in the design.

Requirements
Must have
• it must be elegante

```html
<!DOCTYPE html>
<html lang="en">
<head>
<meta charset="utf-8">
<title>Clara Voss Makeup – Business Card</title>
<link rel="stylesheet" href="https://fonts.googleapis.com/css2?family=Dancing+Script:wght@400&display=swap">
<style>
  :root {
    --backdrop: #e7e5e2;
    --card-black: #0b0b0b;
    --pattern-dark: #1a1a1a;
    --pattern-mid: #262626;
    --ink-white: #f4f4f4;
    --card-shadow: rgba(0, 0, 0, 0.28);
  }
  * { box-sizing: border-box; margin: 0; padding: 0; }
  html, body {
    width: 1200px;
    height: 1200px;
    overflow: hidden;
    background: var(--backdrop);
  }
  .canvas {
    position: relative;
    width: 1200px;
    height: 1200px;
  }
  .card {
    position: absolute;
    left: 190px;
    width: 820px;
    height: 468px;
    border-radius: 26px;
    background: var(--card-black);
    overflow: hidden;
    box-shadow: 0 14px 34px var(--card-shadow);
  }
  .card--front { top: 100px; }
  .card--back { top: 632px; }
  .card__pattern {
    position: absolute;
    inset: 0;
    background:
      radial-gradient(ellipse at 50% 45%, var(--pattern-mid) 0%, var(--pattern-dark) 45%, var(--card-black) 100%);
  }
  .card--back .card__pattern {
    background:
      linear-gradient(180deg, var(--pattern-mid) 0%, var(--pattern-dark) 40%, var(--card-black) 72%);
  }
  .brand-name {
    position: absolute;
    left: 0;
    right: 0;
    top: 50%;
    transform: translateY(-50%);
    text-align: center;
    font-family: "Dancing Script", cursive;
    font-weight: 400;
    font-size: 92px;
    color: var(--ink-white);
    letter-spacing: 1px;
  }
  .contact {
    position: absolute;
    left: 80px;
    right: 80px;
    bottom: 52px;
    font-family: "Dancing Script", cursive;
    font-weight: 400;
    color: var(--ink-white);
  }
  .contact__row {
    display: flex;
    justify-content: space-between;
    font-size: 30px;
    line-height: 1.5;
  }
  .contact__row span { width: 50%; }
  .contact__row span + span { text-align: right; }
  .contact__address {
    margin-top: 12px;
    font-size: 34px;
    text-align: center;
  }
</style>
</head>
<body>
<main class="canvas">
  <section class="card card--front" aria-label="Business card front">
    <div class="card__pattern" role="img" aria-label="Subtle dark tonal floral tile pattern"></div>
    <p class="brand-name">Clara Voss</p>
  </section>

  <section class="card card--back" aria-label="Business card back">
    <div class="card__pattern" role="img" aria-label="Subtle dark tonal floral tile pattern fading downward"></div>
    <div class="contact">
      <p class="contact__row"><span>T: +100 555 0142</span><span>F: +100 555 0199</span></p>
      <p class="contact__row"><span>claravoss@mail.com</span><span>www.claravoss.com</span></p>
      <p class="contact__address">Suite 4, Linden Avenue, Fairview, NY 10234</p>
    </div>
  </section>
</main>
</body>
</html>
```